Radiant Harvest Gathering 2021

I am looking to create a flyer for a one day prayer retreat our church is organizing. This flyer will be posted on social media, websites, mobile apps, and will also be printed so it can be mailed to people.

I am looking for something professional, with good use of our logo and band colors (logo colors).

I am counting on the designer's skill, creativity, art and knowledge of media communication to produce a flyer that will effectively and quickly convey the message we are trying to spread.

CONTENT OF THE FLYER:
Event title: Radiant Harvest Gathering
Date: Tuesday July 2nd, 2021
Time: 11:00AM - 7:00PM
Bellmore Hotel, 4817 Wexley Avenue, Portland, Maine 04109 (Room: Tamarind)
Event Key words to highlight what the event is about: Prayer, Fasting, Worship, Prophecy, Revival.
Key phrases:
A one day prayer retreat.
Jesus Chris is Lord

Contact info:
www.quvello.org
Phone: 207 555 0148
Email: contact@brookmeadow.org

```html
<!DOCTYPE html>
<html lang="en">
<head>
<meta charset="utf-8">
<title>Radiant Harvest Gathering 2021</title>
<link href="https://fonts.googleapis.com/css2?family=Cinzel:wght@500;600&family=Great+Vibes&family=Montserrat:wght@300;400;500;600;700;800&family=Oswald:wght@500&display=swap" rel="stylesheet">
<style>
  :root {
    --navy: #0f3258;
    --orange: #f7941d;
    --orange-soft: #fbb866;
    --white: #ffffff;
    --cream: #fdf1e2;
    --icon-bg: #dcdfe3;
    --page: #e9e9e9;
  }
  * { margin: 0; padding: 0; box-sizing: border-box; }
  html, body { width: 1200px; height: 1200px; overflow: hidden; background: var(--page); }
  .flyer {
    position: absolute; left: 155px; top: 25px;
    width: 967px; height: 1250px;
    transform: scale(0.92); transform-origin: top left;
    background: var(--white); overflow: hidden;
    font-family: "Montserrat", sans-serif; color: var(--navy);
  }
  .backdrop { position: absolute; inset: 0; }
  .abs { position: absolute; white-space: nowrap; }

  .brand-name { left: 88px; top: 138px; font-family: "Cinzel", serif; font-weight: 600; font-size: 78px; color: var(--navy); letter-spacing: 1px; }

  .title-script { left: 70px; top: 462px; font-family: "Great Vibes", cursive; font-size: 86px; color: var(--white); z-index: 3; }
  .title-main { left: 68px; top: 505px; font-family: "Oswald", sans-serif; font-weight: 500; font-size: 232px; line-height: 1; color: var(--orange); transform: scaleX(0.51); transform-origin: left top; letter-spacing: -2px; }
  .sr-only { position: absolute; width: 1px; height: 1px; overflow: hidden; clip: rect(0 0 0 0); }
  .cross-v { left: 452px; top: 410px; width: 26px; height: 308px; background: var(--orange); }
  .cross-h { left: 358px; top: 452px; width: 158px; height: 30px; background: var(--orange); }
  .title-sub { left: 73px; top: 727px; font-weight: 800; font-size: 27px; letter-spacing: 17px; color: var(--white); }
  .divider { left: 182px; top: 804px; width: 164px; height: 3px; background: var(--white); }
  .key-phrase { left: 75px; top: 828px; font-family: "Cinzel", serif; font-weight: 500; font-size: 36px; color: var(--orange); }

  .calendar { left: 551px; top: 452px; width: 98px; height: 100px; background: var(--white); border-radius: 6px; overflow: hidden; }
  .calendar-head { height: 34px; background: var(--orange); display: flex; justify-content: space-between; align-items: flex-end; padding: 0 6px 3px; font-weight: 700; font-size: 15px; color: var(--navy); }
  .calendar-day { text-align: center; font-weight: 700; font-size: 54px; line-height: 62px; color: var(--orange); }
  .calendar-ring { top: 444px; width: 7px; height: 20px; background: var(--navy); border: 2px solid var(--white); border-radius: 4px; }

  .day { left: 670px; top: 452px; font-weight: 700; font-size: 52px; color: var(--white); }
  .time { left: 670px; top: 520px; font-weight: 700; font-size: 22px; color: var(--white); }
  .time span { color: var(--orange); }
  .pin { left: 551px; top: 582px; }
  .venue { left: 593px; top: 580px; font-weight: 500; font-size: 30px; color: var(--white); letter-spacing: .5px; }
  .address { left: 593px; top: 618px; font-weight: 300; font-size: 17px; line-height: 23px; color: var(--white); }

  .retreat { left: 584px; top: 778px; width: 296px; text-align: center; }
  .retreat-rule { width: 118px; height: 4px; background: var(--orange-soft); margin: 0 auto; }
  .retreat-small { font-weight: 300; font-size: 32px; line-height: 40px; margin-top: 10px; }
  .retreat-big { font-weight: 800; font-size: 50px; line-height: 50px; }
  .retreat-big:last-of-type { margin-bottom: 12px; }

  .focus-list { left: 58px; top: 1030px; display: flex; list-style: none; }
  .focus-item { display: flex; align-items: center; font-weight: 300; font-size: 23px; margin-right: 24px; }
  .focus-icon { width: 57px; height: 57px; border-radius: 50%; background: var(--icon-bg); display: flex; align-items: center; justify-content: center; margin-right: 8px; }

  .contact { left: 56px; top: 1140px; font-size: 23px; }
  .contact-row { display: flex; align-items: center; height: 34px; }
  .contact-row svg { margin-right: 10px; }
  .contact-row strong { font-weight: 700; }
  .contact-row .light { font-weight: 300; }
  .contact-heading { left: 607px; top: 1172px; font-weight: 700; font-size: 22px; color: var(--white); letter-spacing: .5px; }
</style>
</head>
<body>
<main class="flyer">
  <svg class="backdrop" width="967" height="1250" viewBox="0 0 967 1250">
    <defs>
      <linearGradient id="photoTone" x1="0" y1="0" x2="1" y2="1">
        <stop offset="0" stop-color="#3f4f66"/><stop offset=".5" stop-color="#6b5241"/><stop offset="1" stop-color="#4a3528"/>
      </linearGradient>
    </defs>
    <path d="M0,225 C170,330 360,310 480,255 L967,255 L967,760 L880,800 L570,925 Q300,990 0,945 Z" fill="var(--navy)"/>
    <path d="M425,0 C440,200 560,360 760,380 C860,390 930,370 967,345 L967,0 Z" fill="#5a4638" stroke="var(--white)" stroke-width="36"/>
    <path role="img" aria-label="Photo of people holding hands in prayer around a wooden table" d="M425,0 C440,200 560,360 760,380 C860,390 930,370 967,345 L967,0 Z" fill="url(#photoTone)"/>
    <circle cx="732" cy="858" r="176" fill="var(--white)"/>
    <circle cx="732" cy="858" r="148" fill="var(--orange)"/>
    <path d="M0,1160 Q260,1085 570,1175 L570,1250 L0,1250 Z" fill="var(--cream)"/>
    <path d="M448,1250 Q690,1105 967,1163 L967,1250 Z" fill="var(--navy)"/>
  </svg>

  <div class="abs brand-name">QUVELLO</div>

  <div class="abs cross-v"></div>
  <div class="abs cross-h"></div>
  <h1>
    <span class="abs title-script">Radiant</span>
    <span class="abs title-main">HARVES<span class="sr-only">T</span></span>
  </h1>
  <div class="abs title-sub">GATHERING</div>
  <div class="abs divider"></div>
  <div class="abs key-phrase">JESUS CHRIS IS LORD</div>

  <div class="abs calendar">
    <div class="calendar-head"><span>JUL.</span><span style="font-weight:500">2021</span></div>
    <div class="calendar-day">02</div>
  </div>
  <div class="abs calendar-ring" style="left:570px"></div>
  <div class="abs calendar-ring" style="left:621px"></div>
  <div class="abs day">Tuesday</div>
  <div class="abs time">at <span>11:00AM - 7:00PM</span></div>

  <svg class="abs pin" width="30" height="42" viewBox="0 0 30 42">
    <path d="M15,1 C7,1 1,7 1,15 C1,25 15,41 15,41 C15,41 29,25 29,15 C29,7 23,1 15,1 Z" fill="var(--orange)"/>
    <circle cx="15" cy="15" r="5" fill="var(--navy)"/>
  </svg>
  <div class="abs venue">BELLMORE HOTEL</div>
  <div class="abs address">4817 Wexley Avenue, Portland, ME 04109<br>(Room: Tamarind)</div>

  <div class="abs retreat">
    <div class="retreat-rule"></div>
    <div class="retreat-small">A ONE DAY</div>
    <div class="retreat-big">PRAYER</div>
    <div class="retreat-big">RETREAT</div>
    <div class="retreat-rule"></div>
  </div>

  <ul class="abs focus-list">
    <li class="focus-item"><span class="focus-icon"><svg width="30" height="34" viewBox="0 0 30 34"><path d="M15,2 L9,16 L5,30 L13,31 L15,20 L17,31 L25,30 L21,16 Z" fill="var(--navy)"/></svg></span>Prayer</li>
    <li class="focus-item"><span class="focus-icon"><svg width="36" height="36" viewBox="0 0 36 36"><circle cx="18" cy="18" r="14" fill="none" stroke="var(--navy)" stroke-width="3"/><circle cx="18" cy="18" r="7" fill="none" stroke="var(--navy)" stroke-width="2"/><line x1="8" y1="8" x2="28" y2="28" stroke="var(--navy)" stroke-width="3"/></svg></span>Fasting</li>
    <li class="focus-item"><span class="focus-icon"><svg width="40" height="30" viewBox="0 0 40 30"><path d="M2,4 L10,14 L14,28 L19,28 L16,12 L6,2 Z M38,4 L30,14 L26,28 L21,28 L24,12 L34,2 Z" fill="var(--navy)"/></svg></span>Worship</li>
    <li class="focus-item"><span class="focus-icon"><svg width="36" height="24" viewBox="0 0 36 24"><path d="M2,12 Q18,-2 34,12 Q18,26 2,12 Z" fill="none" stroke="var(--navy)" stroke-width="2.5"/><circle cx="18" cy="12" r="5" fill="var(--navy)"/></svg></span>Prophecy</li>
    <li class="focus-item"><span class="focus-icon"><svg width="24" height="34" viewBox="0 0 24 34"><path d="M3,2 H21 M3,32 H21 M5,2 C5,12 19,12 19,17 C19,22 5,22 5,32 M19,2 C19,12 5,12 5,17 C5,22 19,22 19,32" fill="none" stroke="var(--navy)" stroke-width="2.5"/></svg></span>Revival</li>
  </ul>

  <div class="abs contact">
    <div class="contact-row">
      <svg width="24" height="24" viewBox="0 0 24 24"><circle cx="12" cy="12" r="11" fill="none" stroke="var(--orange)" stroke-width="1.5"/><rect x="6" y="8" width="12" height="9" fill="none" stroke="var(--orange)" stroke-width="1.5"/><path d="M6,8 L12,13 L18,8" fill="none" stroke="var(--orange)" stroke-width="1.5"/></svg>
      <span class="light">contact@brookmeadow.org</span>
    </div>
    <div class="contact-row">
      <svg width="24" height="24" viewBox="0 0 24 24"><circle cx="12" cy="12" r="11" fill="none" stroke="var(--orange)" stroke-width="1.5"/><path d="M8,6 L10,6 L11,9 L9.5,10.5 Q11,13.5 13.5,14.5 L15,13 L18,14 L18,16 Q17,18 15,18 Q8,16 6,9 Q6,7 8,6 Z" fill="var(--orange)"/></svg>
      <strong>207 555 0148</strong>
      <svg width="24" height="24" viewBox="0 0 24 24" style="margin-left:16px"><circle cx="12" cy="12" r="11" fill="none" stroke="var(--orange)" stroke-width="1.5"/><path d="M9,6 L9,17 L12,14 L14,18 L16,17 L14,13 L18,13 Z" fill="var(--orange)"/></svg>
      <span class="light">www.<strong>quvello</strong>.org</span>
    </div>
  </div>
  <div class="abs contact-heading">CONTACT INFORMATION</div>
</main>
</body>
</html>
```